Real Estate "For Sale" Sign for construction company

We need a sign that we can use to hang on a post and place on the road when we sell a property. The sign will be simple and will need to mainly feature our logo (files attached), as well as the words "For Sale", and then our phone number "(555) 617 3489". The sign will hang on a post that'll look something like the attached picture.

Target Market(s)

Home buyers

Industry/Entity Type

Real Estate

Font styles to use
Serif
Sans Serif

Colors
0054AA
0677BA
7BADD7
CADEEF
E8F1F8
0094D4
00A9DD
6FCCEA
C7EBF8
E9F6FB

Requirements
Must have
• For Sale & our phone number

```html
<!DOCTYPE html>
<html lang="en">
<head>
<meta charset="UTF-8">
<title>For Sale Yard Sign</title>
<link href="https://fonts.googleapis.com/css2?family=Crimson+Text:wght@700&family=Montserrat:wght@400&display=swap" rel="stylesheet">
<style>
  :root {
    --page-bg: #ffffff;
    --band-top: #42c7f5;
    --band-phone: #17a4dd;
    --band-bottom: #8dd7f7;
    --headline: #0054aa;
    --phone-text: #ffffff;
    --brand: #0677ba;
  }
  html, body {
    margin: 0;
    padding: 0;
    width: 1200px;
    height: 1200px;
    overflow: hidden;
    background: var(--page-bg);
  }
  .canvas {
    position: relative;
    width: 1200px;
    height: 1200px;
  }
  .sign {
    position: absolute;
    left: 230px;
    top: 74px;
    width: 740px;
    height: 1052px;
    display: flex;
    flex-direction: column;
  }
  .sign__headline-band {
    height: 439px;
    background: var(--band-top);
    display: flex;
    flex-direction: column;
    align-items: center;
    color: var(--headline);
    font-family: "Crimson Text", Georgia, serif;
    font-weight: 700;
    line-height: 1;
  }
  .headline__for {
    font-size: 156px;
    letter-spacing: 6px;
    margin-top: 68px;
  }
  .headline__sale {
    font-size: 250px;
    letter-spacing: 8px;
    margin-top: -22px;
    margin-left: 20px;
  }
  .sign__phone-band {
    height: 160px;
    background: var(--band-phone);
    display: flex;
    align-items: center;
    justify-content: center;
  }
  .phone {
    font-family: "Crimson Text", Georgia, serif;
    font-weight: 700;
    font-size: 86px;
    color: var(--phone-text);
    letter-spacing: 1px;
    margin-top: -6px;
  }
  .sign__brand-band {
    flex: 1;
    background: var(--band-bottom);
    display: flex;
    align-items: center;
    justify-content: center;
  }
  .brand {
    display: flex;
    align-items: center;
    gap: 16px;
    margin-top: -10px;
  }
  .brand__dot {
    width: 30px;
    height: 30px;
    border-radius: 50%;
    background: var(--brand);
  }
  .brand__name {
    font-family: "Montserrat", Arial, sans-serif;
    font-weight: 400;
    font-size: 40px;
    color: var(--brand);
  }
</style>
</head>
<body>
<main class="canvas">
  <section class="sign" aria-label="For sale sign">
    <div class="sign__headline-band">
      <span class="headline__for">FOR</span>
      <span class="headline__sale">SALE</span>
    </div>
    <div class="sign__phone-band">
      <span class="phone">(555) 617 3489</span>
    </div>
    <div class="sign__brand-band">
      <div class="brand">
        <span class="brand__dot"></span>
        <span class="brand__name">Ridgeline Crest Homes</span>
      </div>
    </div>
  </section>
</main>
</body>
</html>
```